kiPlume Landing Page 2

Edit the attached page to make it more visually appealing and professional. This page is a landing page that will direct our viewers to our rallyvant page. The join buttons definitely need to be changed, as well as fonts for the whole page. Please put rallyvant logo on the "join us" button, and put chatterpod and blipster with logos on the bottom center. If there are any further questions please ask us. http://kiplume.moravist.com/hands.html

Target Market(s)

Middle class Americans ages 20-35.

Industry/Entity Type

It Professional

```html
<!DOCTYPE html>
<html lang="en">
<head>
<meta charset="utf-8">
<title>Landing Page – You Are the Change You Seek</title>
<link rel="stylesheet" href="https://fonts.googleapis.com/css2?family=Bebas+Neue&family=Playfair+Display+SC:wght@400&display=swap">
<style>
  :root {
    --bg-deep: #15231f;
    --bg-mid: #3e5a4f;
    --bg-light: #6f8a7c;
    --text-light: #ffffff;
    --text-soft: #f1f1ea;
    --gold-light: #e9cf8e;
    --gold: #c9a15a;
    --gold-dark: #a47f3e;
  }
  * { margin: 0; padding: 0; box-sizing: border-box; }
  html, body {
    width: 1200px;
    height: 675px;
    overflow: hidden;
    background: var(--bg-deep);
  }
  .landing {
    position: relative;
    width: 1200px;
    height: 675px;
    overflow: hidden;
    font-family: "Bebas Neue", "Arial Narrow", sans-serif;
    color: var(--text-light);
  }
  .hero-photo {
    position: absolute;
    inset: 0;
    background:
      radial-gradient(ellipse 520px 360px at 640px 330px, rgba(111,138,124,0.75), rgba(62,90,79,0.35) 60%, transparent 100%),
      linear-gradient(160deg, var(--bg-mid) 0%, #2b4139 45%, var(--bg-deep) 100%);
  }
  .brand {
    position: absolute;
    left: 98px;
    top: 68px;
    display: flex;
    align-items: center;
    gap: 9px;
    font-size: 21px;
    letter-spacing: 0.3px;
    line-height: 1;
  }
  .brand-dot {
    width: 23px;
    height: 23px;
    border-radius: 50%;
    background: var(--text-light);
  }
  .headline {
    position: absolute;
    top: 176px;
    left: 0;
    width: 1200px;
    text-align: center;
    font-size: 75px;
    font-weight: 400;
    letter-spacing: 0.5px;
    line-height: 1;
  }
  .tagline {
    position: absolute;
    top: 300px;
    left: 0;
    width: 1200px;
    text-align: center;
    font-family: "Playfair Display SC", "Times New Roman", serif;
    font-size: 29px;
    line-height: 49px;
    color: var(--text-soft);
  }
  .actions { position: absolute; inset: 0; pointer-events: none; }
  .action {
    position: absolute;
    display: flex;
    align-items: center;
    text-decoration: none;
    pointer-events: auto;
    background: linear-gradient(180deg, var(--gold-light) 0%, var(--gold) 55%, var(--gold-dark) 100%);
    -webkit-background-clip: text;
    background-clip: text;
    color: transparent;
  }
  .action svg { display: block; }
  .action-join {
    left: 347px;
    top: 436px;
    font-size: 60px;
    line-height: 1;
    gap: 24px;
  }
  .action-video {
    left: 690px;
    top: 451px;
    font-size: 31px;
    line-height: 1;
    gap: 16px;
  }
  .social {
    position: absolute;
    top: 555px;
    left: 0;
    width: 1200px;
    display: flex;
    justify-content: center;
    list-style: none;
    padding-left: 22px;
  }
  .social-item { width: 61px; display: flex; justify-content: center; }
  .social-item a {
    display: flex;
    flex-direction: column;
    align-items: center;
    gap: 14px;
    text-decoration: none;
    color: var(--text-light);
    font-size: 15px;
    letter-spacing: 0.2px;
    line-height: 1;
    white-space: nowrap;
  }
  .social-dot {
    width: 24px;
    height: 24px;
    border-radius: 50%;
    background: var(--text-light);
  }
</style>
</head>
<body>
  <main class="landing">
    <div class="hero-photo" role="img" aria-label="Close-up photograph of two weathered, wrinkled hands clasped together, toned in dark green"></div>

    <div class="brand">
      <span class="brand-dot"></span>
      <span class="brand-name">YOUR LOGO HERE</span>
    </div>

    <h1 class="headline">YOU ARE THE CHANGE YOU SEEK.</h1>

    <p class="tagline">Protecting your family and your<br>future requires your action.</p>

    <nav class="actions">
      <a class="action action-join" href="#">
        <span>JOIN US</span>
        <svg width="24" height="38" viewBox="0 0 24 38" aria-hidden="true">
          <polyline points="4,4 19,19 4,34" fill="none" stroke="#d2ab63" stroke-width="5" stroke-linecap="round" stroke-linejoin="round"/>
        </svg>
      </a>
      <a class="action action-video" href="#">
        <span>WATCH VIDEO</span>
        <svg width="15" height="24" viewBox="0 0 15 24" aria-hidden="true">
          <polyline points="3,3 12,12 3,21" fill="none" stroke="#d2ab63" stroke-width="3.2" stroke-linecap="round" stroke-linejoin="round"/>
        </svg>
      </a>
    </nav>

    <ul class="social">
      <li class="social-item"><a href="#"><span class="social-dot"></span><span>CHATTERPOD</span></a></li>
      <li class="social-item"><a href="#"><span class="social-dot"></span><span>RALLYVANT</span></a></li>
      <li class="social-item"><a href="#"><span class="social-dot"></span><span>BLIPSTER</span></a></li>
    </ul>
  </main>
</body>
</html>
```